Brightmere Pictures Business Card

Hello,

i would like to have a dynamic, creative but tasteful card, colour used, front and back. I have attached a sample card that I liked very much from another individual to give you an idea of the theme/approach, but not colour. Ideally the graphic elements of the Brightmere Logo are brought into the design.

Target Market(s)

North America

Industry/Entity Type

Film Production

Contact Information for Business Card

Nadia Pellwick
President/Founder
Brightmere Pictures Inc.
403 555 2917
nadia@brightmerepictures.tv

Font styles to use
Sans Serif

Colors
6b449b
5c5c5c
fdfdfd
000000

Requirements
Must have
• Logo, name, Company name, email and cell number. no Address line to be included.
Should not have
• any unrelated GFX elements, serif fonts

```html
<!DOCTYPE html>
<html lang="en">
<head>
<meta charset="utf-8">
<title>Brightmere Pictures Business Card</title>
<link rel="stylesheet" href="https://fonts.googleapis.com/css2?family=Open+Sans:wght@400;600;700;800&display=swap">
<style>
  :root {
    --backdrop: #d4d4d4;
    --paper: #f1f1f1;
    --brand-purple: #5c2a8e;
    --accent-purple: #6b449b;
    --ink-grey: #5c5c5c;
    --ink-dark: #1a1a1a;
    --white: #fdfdfd;
  }
  * { margin: 0; padding: 0; box-sizing: border-box; }
  html, body {
    width: 1064px;
    height: 1200px;
    overflow: hidden;
    background: var(--backdrop);
    font-family: "Open Sans", sans-serif;
  }
  .canvas { position: relative; width: 1064px; height: 1200px; }

  .card {
    position: absolute;
    width: 630px;
    height: 390px;
  }
  .card-front {
    left: 265px;
    top: 141px;
    background: var(--paper);
    border-radius: 0 195px 195px 0;
  }
  .card-back {
    left: 233px;
    top: 584px;
    background: var(--brand-purple);
    border-radius: 195px 0 0 195px;
  }

  .wordmark {
    position: absolute;
    font-family: "Open Sans", sans-serif;
    font-weight: 800;
    line-height: 1;
  }
  .wordmark-name { display: block; letter-spacing: -2px; }
  .wordmark-sub {
    display: block;
    text-align: right;
    letter-spacing: 9px;
    margin-right: -9px;
  }
  .card-front .wordmark { left: 32px; top: 52px; color: var(--ink-grey); }
  .card-front .wordmark-name { font-size: 66px; }
  .card-front .wordmark-sub { font-size: 16px; margin-top: 4px; }

  .card-back .wordmark { left: 128px; top: 138px; color: var(--white); }
  .card-back .wordmark-name { font-size: 74px; }
  .card-back .wordmark-sub { font-size: 19px; margin-top: 4px; }

  .contact { position: absolute; left: 32px; top: 183px; color: var(--ink-dark); }
  .contact-name {
    font-size: 16px;
    font-weight: 600;
    letter-spacing: 0.5px;
    color: var(--accent-purple);
    text-transform: uppercase;
  }
  .contact-title { font-size: 15.5px; margin-top: 6px; }
  .contact-company { font-size: 15.5px; margin-top: 32px; padding-left: 3px; }
  .contact-lines { list-style: none; margin-top: 14px; font-size: 15.5px; }
  .contact-lines li { display: flex; align-items: center; gap: 8px; height: 23px; }
  .contact-lines svg { flex: none; }
</style>
</head>
<body>
<main class="canvas">

  <section class="card card-front" aria-label="Card front">
    <div class="wordmark">
      <span class="wordmark-name">brightmere</span>
      <span class="wordmark-sub">PICTURES</span>
    </div>

    <div class="contact">
      <p class="contact-name">Nadia Pellwick</p>
      <p class="contact-title">President/Founder</p>
      <p class="contact-company">Brightmere Pictures Inc.</p>
      <ul class="contact-lines">
        <li>
          <svg width="11" height="15" viewBox="0 0 11 15" aria-hidden="true">
            <rect x="1" y="1" width="9" height="13" rx="1.5" fill="none" stroke="#6b449b" stroke-width="1.8"/>
            <rect x="4" y="11" width="3" height="1.4" fill="#6b449b"/>
          </svg>
          <span>403 555 2917</span>
        </li>
        <li>
          <svg width="12" height="9" viewBox="0 0 12 9" aria-hidden="true">
            <rect x="0" y="0" width="12" height="9" fill="#6b449b"/>
            <polyline points="0.5,0.5 6,5 11.5,0.5" fill="none" stroke="#f1f1f1" stroke-width="1"/>
          </svg>
          <span>nadia@brightmerepictures.tv</span>
        </li>
      </ul>
    </div>
  </section>

  <section class="card card-back" aria-label="Card back">
    <div class="wordmark">
      <span class="wordmark-name">brightmere</span>
      <span class="wordmark-sub">PICTURES</span>
    </div>
  </section>

</main>
</body>
</html>
```